Classy, Elegant, Simple Business Card Design

Looking to have a classy, simple, and elegant design. Want a top notch designed business card. I really like the look of the new brivo credit card. I also like the design I attached. I am trying to reach 21-29 year old females for booking us for there wedding or event. We offer Disc Jockey Service, Photo Booth Rentals, and Uplighting .

Target Market(s)

21-28 year old females

Contact Information for Business Card

Has to have logo, website, email, and phone number

Font styles to use
Other font styles liked:
• open to font choice, modern, clean
Designer to choose
33a6d7
0791cd
0555a3
ffffff

Requirements
Must have
• Has to have logo, website, email, and phone number
Nice to have
• I really like the design of the new brivo credit card. I also included my logo and some designs I like
Should not have
• clutter or too much info

```html
<!DOCTYPE html>
<html lang="en">
<head>
<meta charset="utf-8">
<title>Tidewell Event Group – Business Card</title>
<link rel="stylesheet" href="https://fonts.googleapis.com/css2?family=Jost:wght@400;500&display=swap">
<style>
  :root {
    --backdrop: #404040;
    --card: #262626;
    --ink: #ffffff;
    --mark: #c9c9c9;
  }
  * { box-sizing: border-box; margin: 0; padding: 0; }
  html, body {
    width: 1200px;
    height: 900px;
    overflow: hidden;
    background: var(--backdrop);
    font-family: "Jost", "Futura", sans-serif;
    color: var(--ink);
  }
  .stage {
    position: relative;
    width: 1200px;
    height: 900px;
  }
  .card {
    position: absolute;
    left: 297px;
    width: 608px;
    height: 348px;
    border-radius: 18px;
    background: var(--card);
  }
  .card--front { top: 84px; }
  .card--back { top: 467px; }

  .front-name {
    position: absolute;
    left: 0;
    right: 0;
    top: 136px;
    text-align: center;
    font-size: 66px;
    font-weight: 500;
    line-height: 1;
    letter-spacing: 1px;
    color: var(--mark);
  }

  .brand-name {
    position: absolute;
    right: 43px;
    top: 64px;
    text-align: right;
    font-weight: 500;
    color: var(--mark);
    line-height: 1;
  }
  .brand-name__main {
    display: block;
    font-size: 30px;
    letter-spacing: 1px;
  }
  .brand-name__sub {
    display: block;
    margin-top: 4px;
    font-size: 13px;
    letter-spacing: 7px;
    margin-right: -7px;
  }

  .contact {
    position: absolute;
    left: 42px;
    top: 186px;
  }
  .contact__name {
    font-size: 21px;
    font-weight: 500;
    letter-spacing: 0.5px;
    margin-bottom: 12px;
  }
  .contact__line {
    font-size: 16px;
    font-weight: 400;
    line-height: 24.5px;
    letter-spacing: 0.3px;
  }
</style>
</head>
<body>
<main class="stage">
  <section class="card card--front">
    <p class="front-name">Tidewell</p>
  </section>

  <section class="card card--back">
    <p class="brand-name">
      <span class="brand-name__main">TIDEWELL</span>
      <span class="brand-name__sub">EVENT GROUP</span>
    </p>
    <div class="contact">
      <p class="contact__name">Daniel R. Hale</p>
      <p class="contact__line">555 014 2290</p>
      <p class="contact__line">info@tidewelleventgroup.com</p>
      <p class="contact__line">www.tidewelleventgroup.com</p>
    </div>
  </section>
</main>
</body>
</html>
```